FinTech company looking to revamp and expand client-facing interface for our financial models

Halvern Ledgerworks currently has a very simple website that allows clients to interact with our financial models. We are looking to completely redesign the current site and add several extra pages to provide extra functionality. We want the design to have a modern, slick feel, that will work on both a desktop or a tablet. It should be straightforward for clients to move between different pages at any time, and clear from the layout how to interact with the more advanced features. We have included screenshots of existing pages in the attached design brief, as well as sketches of the functionality required by the new pages, but can't provide a direct link to the current site.
Target Market(s)
Professional investors that will be paying to access the interface
Industry/Entity Type
Finance
Number of Pages Required
4 page
Colors
Designer to choose colors to be used in the design.
Look and feel
Each slider illustrates characteristics of the customer's brand and the style your logo design should communicate.

```html
<!DOCTYPE html>
<html lang="en">
<head>
<meta charset="utf-8">
<title>Halvern Ledgerworks – Models</title>
<link href="https://fonts.googleapis.com/css2?family=Roboto:wght@400;500;700&display=swap" rel="stylesheet">
<style>
  :root {
    --navy: #1c2331;
    --page: #e6e7e9;
    --card: #ffffff;
    --ink: #1b1b1b;
    --muted: #9a9a9a;
    --row-alt: #fbf9ef;
    --rule: #e4e4e4;
    --field: #f2f2f2;
    --field-border: #c9c9c9;
  }
  * { box-sizing: border-box; margin: 0; padding: 0; }
  html, body { width: 1200px; height: 857px; overflow: hidden; }
  body { background: var(--page); font-family: "Roboto", Arial, sans-serif; color: var(--ink); position: relative; }

  .app-card { position: absolute; left: 40px; top: 92px; width: 1121px; height: 673px; background: var(--card); border-radius: 24px; overflow: hidden; }

  .top-bar { position: absolute; left: 0; top: 0; width: 100%; height: 78px; background: var(--navy); }
  .brand { position: absolute; left: 80px; top: 26px; color: #fff; font-weight: 700; font-size: 23px; letter-spacing: .3px; }
  .period { position: absolute; top: 31px; color: #fff; font-size: 14px; }
  .period-250 { left: 234px; } .period-83 { left: 284px; } .period-42 { left: 330px; }

  .nav-tab { position: absolute; top: 0; height: 78px; width: 130px; color: #fff; font-size: 14px; text-align: center; }
  .nav-tab svg { display: block; margin: 18px auto 8px; width: 20px; height: 20px; fill: currentColor; }
  .nav-tab.is-active { background: var(--card); color: var(--navy); border-radius: 22px 22px 0 0; width: 103px; }
  .tab-models { left: 584px; } .tab-sensitivities { left: 706px; } .tab-favourites { left: 848px; }

  .filter-label { position: absolute; top: 137px; font-size: 13px; font-weight: 700; }
  .filter-label small { font-size: 8px; font-weight: 400; vertical-align: 6px; }
  .filter-tiny { position: absolute; left: 103px; top: 143px; font-size: 8px; }
  .filter-input { position: absolute; top: 130px; width: 173px; height: 31px; background: var(--field); border: 1px solid var(--field-border); border-radius: 8px; color: var(--muted); font-size: 11px; padding: 8px 12px; }

  .models-table { position: absolute; left: 31px; top: 256px; width: 1054px; border-collapse: separate; border-spacing: 0; font-size: 12px; }
  .models-table th { background: var(--navy); color: #fff; font-weight: 700; font-size: 15px; height: 43px; border-radius: 8px; border-left: 1px solid #fff; border-right: 1px solid #fff; }
  .models-table td { vertical-align: top; line-height: 16px; padding-top: 13px; border-right: 1px solid var(--rule); border-bottom: 1px solid var(--rule); height: 56px; }
  .models-table td:first-child { border-left: 1px solid var(--rule); text-align: center; }
  .models-table tr.first td { height: 70px; padding-top: 25px; }
  .models-table tbody tr:nth-child(even) td { background: var(--row-alt); }
  .sort-caret { display: inline-block; width: 0; height: 0; border: 4px solid transparent; border-top: 5px solid #fff; margin-left: 8px; vertical-align: -1px; }

  .view-more { position: absolute; left: 499px; top: 613px; width: 123px; height: 41px; background: var(--navy); color: #fff; border-radius: 21px; font-size: 14px; text-align: center; line-height: 41px; }
</style>
</head>
<body>
<main class="app-card">
  <header class="top-bar">
    <div class="brand">HALVERN</div>
    <span class="period period-250">250D</span>
    <span class="period period-83">83D</span>
    <span class="period period-42">42D</span>

    <div class="nav-tab tab-models is-active">
      <svg viewBox="0 0 20 20"><path d="M10 2 1 10h2.5v8h5v-5h3v5h5v-8H19z"/></svg>Models
    </div>
    <div class="nav-tab tab-sensitivities">
      <svg viewBox="0 0 20 20"><circle cx="7" cy="7" r="4.5" fill="none" stroke="#fff" stroke-width="2.4" stroke-dasharray="2 1.5"/><circle cx="14" cy="14" r="3.5" fill="none" stroke="#fff" stroke-width="2.2" stroke-dasharray="1.8 1.3"/><circle cx="7" cy="7" r="1.4"/><circle cx="14" cy="14" r="1.1"/></svg>Sensitivities
    </div>
    <div class="nav-tab tab-favourites">
      <svg viewBox="0 0 20 20"><path d="M10 1.5l2.6 5.6 6.1.7-4.5 4.2 1.2 6L10 15l-5.4 3 1.2-6-4.5-4.2 6.1-.7z"/></svg>Favourites
    </div>
  </header>

  <span class="filter-tiny">Quality</span>
  <span class="filter-label" style="left:158px">Threshold:</span>
  <div class="filter-input" style="left:236px">-10</div>

  <span class="filter-label" style="left:470px">Abs. <small>Stat</small></span>
  <span class="filter-label" style="left:534px">Threshold:</span>
  <div class="filter-input" style="left:613px">-10</div>

  <table class="models-table">
    <colgroup>
      <col style="width:104px"><col style="width:106px"><col style="width:102px"><col style="width:77px">
      <col style="width:77px"><col style="width:77px"><col style="width:86px"><col style="width:86px">
      <col style="width:79px"><col style="width:86px"><col style="width:86px"><col style="width:86px">
    </colgroup>
    <thead>
      <tr><th>ID<span class="sort-caret"></span></th><th>Sector</th><th>Time</th><th>Quality</th><th>Star 1</th><th>Star 2</th><th>Star 3</th><th>Star 4</th><th>Star 5</th><th>Star 6</th><th>Star 7</th><th>Star 8</th></tr>
    </thead>
    <tbody>
      <tr class="first"><td>Model 1</td><td style="padding-left:17px">Materials</td><td style="padding-left:11px">2019-07-03<br>12:15:00.000</td><td style="padding-left:14px">30.2288</td><td style="padding-left:12px">2.01574</td><td style="padding-left:19px">23.305</td><td style="padding-left:12px">-0.149368</td><td style="padding-left:19px">22.3054</td><td style="padding-left:16px">4.63714</td><td style="padding-left:16px">0.945706</td><td style="padding-left:17px">2.81949</td><td style="padding-left:19px">2.60858</td></tr>
      <tr><td>Model 2</td><td style="padding-left:17px">Industries</td><td style="padding-left:11px">2019-07-03<br>12:15:00.000</td><td style="padding-left:14px">32.8694</td><td style="padding-left:12px">0.87307</td><td style="padding-left:19px">32.185</td><td style="padding-left:12px">-0.0336927</td><td style="padding-left:19px">33.99111</td><td style="padding-left:16px">11.5693</td><td style="padding-left:16px">-0.472968</td><td style="padding-left:17px">-0.830458</td><td style="padding-left:19px">6.80646</td></tr>
      <tr><td>Model 3</td><td style="padding-left:17px">Consumer<br>Discretionary</td><td style="padding-left:11px">2019-07-03<br>12:15:00.000</td><td style="padding-left:14px">1.66002</td><td style="padding-left:12px">-0.569222</td><td style="padding-left:19px">159.814</td><td style="padding-left:12px">0.0252328</td><td style="padding-left:19px">172.616</td><td style="padding-left:16px">10.2875</td><td style="padding-left:16px">-0.750396</td><td style="padding-left:17px">-0.385309</td><td style="padding-left:19px">4.69146</td></tr>
      <tr><td>Model 4</td><td style="padding-left:17px">Information<br>Technology</td><td style="padding-left:11px">2019-07-03<br>12:15:00.000</td><td style="padding-left:14px">45.685</td><td style="padding-left:12px">0.412148</td><td style="padding-left:19px">202.488</td><td style="padding-left:12px">0.00849232</td><td style="padding-left:19px">205.834</td><td style="padding-left:16px">11.9094</td><td style="padding-left:16px">-0.137913</td><td style="padding-left:17px">0.449595</td><td style="padding-left:19px">3.85106</td></tr>
      <tr><td>Model 5</td><td style="padding-left:17px">Information<br>Technology</td><td style="padding-left:11px">2019-07-03<br>12:15:00.000</td><td style="padding-left:14px">75.7733</td><td style="padding-left:12px">7.06728</td><td style="padding-left:19px">188.605</td><td style="padding-left:12px">0.016913</td><td style="padding-left:19px">181.665</td><td style="padding-left:16px">3.82241</td><td style="padding-left:16px">0.981019</td><td style="padding-left:17px">1.29847</td><td style="padding-left:19px">3.34927</td></tr>
    </tbody>
  </table>

  <div class="view-more">View More</div>
</main>
</body>
</html>
```